EPS Recycling Rpt

Our annual recycling rate report needs a tune up. Our organization helps faciltate expanded polystyrene (EPS) recycling and this 4-page report highlights growth trends and useful information to help readers understand the dynamics of EPS recycling. We need a designer that can recreate the brochure we've published over the past several years with some minor adjustments to accomodate new content.

A PDF of the 2012 report is attached. Header text should reflect 2013 in all cases. Please pay close attention to the new placement of the copy as indicated in the Word file (also attached) as it has been significantly modified from the 2012 version. The color pallette for our branding is provided. Contact us with any questions.

```html
<!DOCTYPE html>
<html lang="en">
<head>
<meta charset="utf-8">
<title>2013 EPS Recycling Rate Report – Cover</title>
<link rel="stylesheet" href="https://fonts.googleapis.com/css2?family=Josefin+Sans:wght@200&family=Montserrat:wght@300;700&display=swap">
<style>
  :root {
    --backdrop: #d9d9d9;
    --paper: #f7f7f5;
    --olive: #9c9a2e;
    --ink-grey: #5a5a5a;
  }
  * { margin: 0; padding: 0; box-sizing: border-box; }
  html, body {
    width: 1200px;
    height: 803px;
    overflow: hidden;
    background: var(--backdrop);
  }
  .cover {
    position: absolute;
    left: 320px;
    top: 39px;
    width: 560px;
    height: 725px;
    background: var(--paper);
    overflow: hidden;
  }
  .year {
    position: absolute;
    left: -34px;
    top: 20px;
    font-family: "Josefin Sans", sans-serif;
    font-weight: 200;
    font-size: 330px;
    line-height: 0.84;
    color: var(--olive);
    letter-spacing: -6px;
  }
  .year span { display: block; }
  .report-title {
    position: absolute;
    left: 392px;
    top: 96px;
    font-family: "Montserrat", sans-serif;
    font-weight: 700;
    font-size: 14px;
    line-height: 1.2;
    letter-spacing: 1.5px;
    text-transform: uppercase;
    color: var(--ink-grey);
  }
  .org-name {
    position: absolute;
    left: 392px;
    top: 452px;
    font-family: "Montserrat", sans-serif;
    font-weight: 300;
    font-size: 20px;
    line-height: 1.2;
    color: var(--ink-grey);
  }
</style>
</head>
<body>
  <main class="cover">
    <h1 class="year" aria-label="2013">
      <span>20</span>
      <span>13</span>
    </h1>
    <p class="report-title">EPS<br>Recycling<br>Rate<br>Report</p>
    <p class="org-name">Polyfoam<br>Recovery Council</p>
  </main>
</body>
</html>
```